Label design for high quality nutritional supplement brand

We need a new label design for our dietary supplement brand "NorlumPlus" from Germany. We sell high-quality nutritional supplements that help improve overall well-being.

All products in our range should receive the new label. You can find our current design on our homepage norlumplus-shop.example. The new design should be completely redesigned and look modern, fresh, high quality, minimalist and clean. We prefer the colors nude, green and earth tones.

The newly created label should contain our NorlumPlus logo. For this reason you will find this file attached. You will also find our current label, which needs to be renewed, in the appendix.

Colors

Designer to choose colors to be used in the design.

Requirements
Must have
• NorlumPlus logo

```html
<!DOCTYPE html>
<html lang="de">
<head>
<meta charset="utf-8">
<title>NorlumPlus Complex – Label</title>
<link rel="stylesheet" href="https://fonts.googleapis.com/css2?family=Inter:wght@400;500&family=Poppins:wght@400;600&family=Open+Sans:wght@400&display=swap">
<style>
  :root {
    --bg-top: #c4c4c4;
    --bg-bottom: #ececec;
    --label-white: #f7f7f7;
    --figure-tone: #e6ddd6;
    --brand-green: #8db640;
    --title-peach: #eab383;
    --title-brown: #b38e6e;
    --band-dark: #7d6e64;
    --band-light: #bcafa6;
    --band-text: #f4efeb;
    --orange-dark: #d4883c;
    --orange-light: #f3c797;
  }
  * { margin: 0; padding: 0; box-sizing: border-box; }
  html, body { width: 1200px; height: 960px; overflow: hidden; }
  body {
    background: linear-gradient(180deg, var(--bg-top) 0%, var(--bg-bottom) 100%);
    font-family: "Poppins", sans-serif;
    position: relative;
  }
  .label {
    position: absolute;
    left: 280px;
    top: 57px;
    width: 640px;
    height: 846px;
    background: var(--label-white);
    box-shadow: 0 10px 30px rgba(0,0,0,0.08);
    display: flex;
    flex-direction: column;
  }
  .label__front {
    position: relative;
    height: 620px;
  }
  .figure-area {
    position: absolute;
    left: 80px;
    right: 80px;
    top: 28px;
    bottom: 0;
    background: linear-gradient(90deg, var(--figure-tone) 0%, var(--label-white) 22%, var(--label-white) 78%, var(--figure-tone) 100%);
  }
  .brand-mark {
    position: absolute;
    left: 0; right: 0;
    top: 205px;
    display: flex;
    justify-content: center;
    align-items: center;
    gap: 12px;
  }
  .brand-mark__dot {
    width: 16px; height: 16px;
    border-radius: 50%;
    background: var(--brand-green);
  }
  .brand-mark__name {
    font-family: "Open Sans", sans-serif;
    font-weight: 400;
    font-size: 40px;
    color: var(--brand-green);
    letter-spacing: 0.5px;
  }
  .product-name {
    position: absolute;
    left: 0; right: 0;
    top: 380px;
    text-align: center;
  }
  .product-name__brand {
    font-size: 62px;
    line-height: 1.1;
    color: var(--title-peach);
    font-weight: 400;
  }
  .product-name__brand strong { font-weight: 600; }
  .product-name__variant {
    font-size: 48px;
    line-height: 1.15;
    color: var(--title-brown);
    font-weight: 400;
  }
  .info-band {
    height: 150px;
    background: linear-gradient(90deg, var(--band-dark) 0%, var(--band-light) 35%, var(--band-light) 65%, var(--band-dark) 100%);
    color: var(--band-text);
    position: relative;
  }
  .info-band__category {
    position: absolute;
    left: 0; right: 0; top: 24px;
    text-align: center;
    font-family: "Inter", sans-serif;
    font-size: 22px;
    letter-spacing: 6px;
    font-weight: 400;
  }
  .info-band__meta {
    position: absolute;
    left: 130px; right: 130px; top: 96px;
    display: flex;
    justify-content: space-between;
    font-family: "Poppins", sans-serif;
    font-size: 19px;
  }
  .info-band__meta b { font-weight: 600; }
  .web-band {
    flex: 1;
    background: linear-gradient(90deg, var(--orange-dark) 0%, var(--orange-light) 45%, var(--orange-light) 60%, var(--orange-dark) 100%);
    display: flex;
    align-items: center;
    justify-content: center;
    font-family: "Poppins", sans-serif;
    font-size: 20px;
    color: #fbf1e6;
    letter-spacing: 0.4px;
  }
</style>
</head>
<body>
  <main class="label">
    <section class="label__front">
      <div class="figure-area" role="img" aria-label="Line illustration of a slim waist silhouette framing the product name"></div>
      <div class="brand-mark">
        <span class="brand-mark__dot"></span>
        <span class="brand-mark__name">NorlumPlus</span>
      </div>
      <h1 class="product-name">
        <div class="product-name__brand">Norlum<strong>Plus</strong></div>
        <div class="product-name__variant">Complex</div>
      </h1>
    </section>
    <section class="info-band">
      <p class="info-band__category">MULTIVITAMIN</p>
      <div class="info-band__meta">
        <span>Inhalt: 83.1g</span>
        <span><b>90</b> Kapseln</span>
      </div>
    </section>
    <footer class="web-band">www.norlumplus-shop.example</footer>
  </main>
</body>
</html>
```